Computer business needs new look.

KELVO Computers has been selling and repairing, servicing computers in northern NSW for 20 years and has now branched out into Surveillance/ CCTV systems Alarm systems and just about anything technical.
We have also changed our area of operation from just the northern rivers to include all of outback New South Wales and Queensland.
We have changed our name slightly to K.E.L.V Bushline Technical Services.I will include my old business card.The Logo can stay or go i am open to all designs.
Updates

facebook page for info https://www.example-social.test/pages/KELVO-Computers/483920571638215?fref=ts The top half of the business card i uploaded looks pink ! it should be white

I should have mentioned this before. My new look cards will become the look of the business. ie: advertising, vehicle sign-writing etc: The look that i think im after is more to large business/corporate look not "PERCY THE FIXER " Probably the main focus is the fact that we service the small towns in outback Australia. " Gumtree Jackson " Not just the big city's Please feel free to through any thing at me and any questions please ask.

I have uploaded a picture that i would like the back of the card to look like. Please have a look and see what you can do.

Reason: I am hoping to get some original designs that i like. So far i have just 1 that i like..there must be more ideas out there.

Target Market(s)

Small to medium business

Industry/Entity Type

Business

Contact Information for Business Card

K.E.L.V Bushline Technical Services
Glen Mortby
1300417266 0451 738205

Requirements
Nice to have
• Back of card to have a list of services
Computer sales
Computer Repairs & Virus removal
Wireless Hotspots
CCTV Installation and repair
Network Design and setup
Troubleshooting

```html
<!DOCTYPE html>
<html lang="en">
<head>
<meta charset="utf-8">
<title>K.E.L.V Bushline Technical Services – Business Card</title>
<link rel="stylesheet" href="https://fonts.googleapis.com/css2?family=Nunito+Sans:wght@300;400;800;900&display=swap">
<style>
  :root {
    --stage: #e9e7e5;
    --card-white: #ffffff;
    --card-brown: #4a1a12;
    --circuit-dark: #2a120b;
    --circuit-mid: #6b3219;
    --brand-red: #e8452a;
    --ink: #2b140e;
    --ink-soft: #3a1d15;
    --on-brown: #f3e9e4;
  }
  * { box-sizing: border-box; margin: 0; padding: 0; }
  html, body {
    width: 1200px;
    height: 1000px;
    overflow: hidden;
    background: var(--stage);
    font-family: "Nunito Sans", Arial, sans-serif;
  }
  .canvas {
    position: relative;
    width: 1200px;
    height: 1000px;
  }
  .card {
    position: absolute;
    top: 190px;
    width: 380px;
    height: 620px;
    overflow: hidden;
    box-shadow: 0 6px 18px rgba(0,0,0,0.18);
  }
  .card--front { left: 170px; background: var(--card-white); }
  .card--back  { left: 650px; background: var(--card-brown); }

  .circuit-photo {
    position: absolute;
    left: 0; top: 0;
    width: 100%;
    height: 262px;
    background: radial-gradient(ellipse at 35% 40%, var(--circuit-mid) 0%, #4a200f 45%, var(--circuit-dark) 100%);
  }

  .brand {
    position: absolute;
    right: 30px;
    text-align: right;
  }
  .brand__name {
    display: block;
    font-weight: 900;
    font-size: 92px;
    line-height: 0.85;
    letter-spacing: -2px;
    color: var(--brand-red);
  }
  .brand__tagline {
    display: block;
    margin-top: 4px;
    font-weight: 800;
    font-size: 13.5px;
    color: var(--brand-red);
  }
  .card--front .brand { top: 188px; }
  .card--back .brand  { top: 432px; }

  .contact {
    position: absolute;
    right: 30px;
    top: 325px;
    text-align: right;
    color: var(--ink-soft);
  }
  .contact__name {
    font-weight: 900;
    font-size: 29px;
    color: var(--ink);
    margin-bottom: 4px;
  }
  .contact__line {
    font-weight: 300;
    font-size: 25px;
    line-height: 1.25;
  }

  .services {
    position: absolute;
    right: 34px;
    top: 72px;
    list-style: none;
    text-align: right;
    color: var(--on-brown);
    font-weight: 300;
    font-size: 20px;
    line-height: 1.2;
  }
</style>
</head>
<body>
<main class="canvas">

  <section class="card card--front" aria-label="Business card front">
    <div class="circuit-photo" role="img" aria-label="Close-up photograph of a copper-toned circuit board"></div>
    <div class="brand">
      <span class="brand__name">kelv</span>
      <span class="brand__tagline">Bushline Technical Services</span>
    </div>
    <div class="contact">
      <p class="contact__name">Glen Mortby</p>
      <p class="contact__line">1300417266</p>
      <p class="contact__line">0451 738205</p>
      <p class="contact__line">glen@kelv.com.au</p>
      <p class="contact__line">www.kelv.com.au</p>
    </div>
  </section>

  <section class="card card--back" aria-label="Business card back">
    <ul class="services">
      <li>Computer Sales</li>
      <li>Computer Repairs</li>
      <li>Virus Removal</li>
      <li>CCTV Installation and Repair</li>
      <li>Alarm Installation</li>
      <li>Network Design and Setup</li>
      <li>Printer Sales and Setup</li>
    </ul>
    <div class="brand">
      <span class="brand__name">kelv</span>
      <span class="brand__tagline">Bushline Technical Services</span>
    </div>
  </section>

</main>
</body>
</html>
```